BRISKWAY ELECTRICAL SIGN

We are wanting a sign to mount on the side of the road to attract peoples attention, it will be 1200mm high by 2400mm wide. We want it to stand out from the others, modern sharp looking, We are an electrical contractor who wants to be the market leader and supplier of choice to our current clients and futre clients.

Industry/Entity Type

Electrical

Colors

Designer to choose colors to be used in the design.

Requirements
Must have
• Name: Briskway Electrical
• Our logo as per uploaded files
• The words: Design - Installation - Maintenance
• Freecall: 0800 342 958
• Mobile : 021 736 4192 (delete mobile number if gets to cluttered)
• Web: www.briskway.net.nz
Should not have
• a light bulb, or plug

```html
<!DOCTYPE html>
<html lang="en">
<head>
<meta charset="utf-8">
<title>Briskway Electrical – Roadside Sign</title>
<link rel="stylesheet" href="https://fonts.googleapis.com/css2?family=Exo+2:wght@600;700;800&display=swap">
<style>
  :root {
    --page-bg: #ffffff;
    --sign-bg: #ffffff;
    --brand-green: #a8cc3a;
    --brand-blue: #3b74c2;
    --text-grey: #5f5f62;
    --faint-trace: #eef2f8;
  }
  * { margin: 0; padding: 0; box-sizing: border-box; }
  html, body {
    width: 1033px; height: 1200px; overflow: hidden;
    background: var(--page-bg);
    font-family: "Exo 2", Arial, sans-serif;
  }
  .canvas { position: relative; width: 1033px; height: 1200px; }
  .sign {
    position: absolute; left: 4px; top: 344px;
    width: 1024px; height: 512px;
    background: var(--sign-bg);
    box-shadow: 0 2px 6px rgba(0,0,0,0.35);
    overflow: hidden;
  }
  .sign-shapes { position: absolute; inset: 0; }
  .trace-area {
    position: absolute; left: 230px; top: 150px; width: 560px; height: 250px;
    background: radial-gradient(ellipse at center, var(--faint-trace) 0%, rgba(255,255,255,0) 70%);
  }
  .web-address {
    position: absolute; left: 82px; top: 256px;
    transform: translate(-50%, -50%) rotate(-90deg);
    color: #ffffff; font-weight: 700; font-size: 38px; letter-spacing: 0.5px;
    white-space: nowrap;
  }
  .brand {
    position: absolute; right: 54px; top: 78px;
    display: flex; align-items: center; gap: 14px;
  }
  .brand-dot { width: 22px; height: 22px; border-radius: 50%; background: var(--brand-green); }
  .brand-name {
    color: var(--brand-blue); font-weight: 800; font-size: 50px; line-height: 1;
    letter-spacing: 0.5px;
  }
  .services {
    position: absolute; right: 34px; top: 206px;
    list-style: none; text-align: right;
  }
  .services li {
    color: var(--text-grey); font-weight: 700; font-size: 41px; line-height: 53px;
    display: flex; justify-content: flex-end; align-items: center; gap: 16px;
  }
  .services li::after {
    content: ""; width: 13px; height: 13px; border-radius: 50%;
    background: var(--brand-green);
  }
  .contacts { position: absolute; left: 666px; top: 388px; }
  .contact {
    display: flex; align-items: center; gap: 16px; height: 52px;
    color: var(--brand-blue); font-weight: 700; font-size: 37px; letter-spacing: 0.5px;
  }
  .contact-icon { width: 44px; height: 44px; flex: none; }
</style>
</head>
<body>
<div class="canvas">
  <section class="sign" aria-label="Briskway Electrical roadside sign">
    <svg class="sign-shapes" width="1024" height="512" viewBox="0 0 1024 512" aria-hidden="true">
      <path class="green-band" d="M0 0 H232 C120 110 110 330 420 512 H0 Z" fill="var(--brand-green)"/>
    </svg>
    <div class="trace-area" role="img" aria-label="Faint circuit board trace pattern in pale blue"></div>

    <div class="web-address">www.briskway.net.nz</div>

    <div class="brand">
      <span class="brand-dot"></span>
      <span class="brand-name">BRISKWAY ELECTRICAL</span>
    </div>

    <ul class="services">
      <li>Design</li>
      <li>Installation</li>
      <li>Maintenance</li>
    </ul>

    <div class="contacts">
      <div class="contact">
        <svg class="contact-icon" viewBox="0 0 44 44" aria-label="Freecall">
          <circle cx="22" cy="22" r="22" fill="var(--brand-blue)"/>
          <path d="M15 12 l5 -1 l3 7 l-3 2 c1 3 3 5 6 6 l2 -3 l7 3 l-1 5 c-10 1 -20 -9 -19 -19z" fill="#fff"/>
        </svg>
        <span>0800 342 958</span>
      </div>
      <div class="contact">
        <svg class="contact-icon" viewBox="0 0 44 44" aria-label="Mobile">
          <circle cx="22" cy="22" r="22" fill="var(--brand-blue)"/>
          <rect x="15" y="10" width="14" height="24" rx="2.5" fill="#fff"/>
          <rect x="17.5" y="13" width="9" height="15" fill="var(--brand-blue)"/>
          <circle cx="22" cy="31" r="1.3" fill="var(--brand-blue)"/>
        </svg>
        <span>021 736 4192</span>
      </div>
    </div>
  </section>
</div>
</body>
</html>
```